Brackenford Fluidworks needs a website describing the repair business we are in.

Brackenford Fluidworks is a full hydraulic repair facility. We have 2 shops. We repair and service all hydraulic cylinders, pneumatic cylinders, hydraulic pumps, motors, valves and gearboxes. Our services range from large industrial plants to the individual that owns one piece of equipment. We also offer removal and install of cylinders. Along with free pick up and delivery, within a certain distance which is usually 100 miles from one of our shops.

With over 30 years experience in the hydraulic business, we can repair or replace any job. There is not a job too big or too small, we service them all.

We have customers that send whole pieces of equipment to us to do complete overhauls on all the hydraulics. Ranging from a country club green roller to a 10 ton boom truck.

Target Market(s)

Industrial plants, road builders, dirt work companies, general contractors, owners of industrial equipment (bulldozers, excavators, loaders, scrapers, motor graders, etc.

Industry/Entity Type

Hydraulic

Number of Pages Required

5+ page

Font styles to use
Sans Serif

Colors
ec1f27
ffffff
aaaaaa

Requirements
Must have
• Information about what we offer and pictures of jobs completed.
Nice to have
• Nice stock photos of jobsites and industrial plants.
Should not have
• Any sort of comical characters.

```html
<!DOCTYPE html>
<html lang="en">
<head>
<meta charset="utf-8">
<title>Brackenford Fluidworks — Hydraulic Repair</title>
<link href="https://fonts.googleapis.com/css2?family=Nunito+Sans:wght@400;600;700;800&display=swap" rel="stylesheet">
<style>
  :root {
    --red: #ec1f27;
    --white: #ffffff;
    --grey: #aaaaaa;
    --ink: #333333;
    --steel-dark: #3a3d40;
    --steel-mid: #6c7073;
    --steel-light: #a9adb0;
  }
  * { box-sizing: border-box; margin: 0; padding: 0; }
  html, body { width: 1200px; height: 900px; overflow: hidden; }
  body { font-family: "Nunito Sans", Arial, sans-serif; background: var(--white); color: var(--ink); }

  .site { position: relative; width: 1200px; height: 900px; }

  /* Header */
  .site-header { position: absolute; top: 0; left: 0; width: 100%; height: 120px; background: var(--white); }
  .brand { position: absolute; left: 60px; top: 52px; display: flex; align-items: center; gap: 10px; }
  .brand-mark { width: 34px; height: 34px; border-radius: 50%; background: var(--red); }
  .brand-name { font-weight: 800; font-size: 15px; line-height: 1.05; color: var(--red); letter-spacing: .5px; text-transform: uppercase; }

  .top-bar { position: absolute; right: 60px; top: 16px; display: flex; align-items: center; gap: 16px; }
  .call { font-size: 13px; font-weight: 700; color: var(--red); display: flex; align-items: center; gap: 6px; }
  .call span { color: var(--ink); font-weight: 600; }
  .social { display: flex; gap: 5px; }
  .social i { width: 16px; height: 16px; border-radius: 50%; background: var(--grey); display: block; }
  .social i:nth-child(2) { background: var(--red); }
  .quote-btn { border: 1.5px solid var(--red); color: var(--red); border-radius: 20px; padding: 7px 18px; font-size: 11px; font-weight: 700; text-transform: uppercase; letter-spacing: .6px; }

  .main-nav { position: absolute; right: 60px; top: 72px; display: flex; gap: 34px; }
  .main-nav a { font-size: 11px; font-weight: 700; text-transform: uppercase; letter-spacing: .8px; color: var(--ink); text-decoration: none; padding-bottom: 6px; }
  .main-nav a.active { color: var(--red); border-bottom: 2px solid var(--red); }

  /* Hero */
  .hero { position: absolute; top: 120px; left: 0; width: 100%; height: 420px; }
  .hero-photo { position: absolute; inset: 0; background: linear-gradient(120deg, var(--steel-dark) 0%, var(--steel-mid) 45%, var(--steel-light) 70%, var(--steel-mid) 100%); }
  .hero-shade { position: absolute; inset: 0; background: linear-gradient(90deg, rgba(0,0,0,.5), rgba(0,0,0,.1)); }
  .hero-copy { position: absolute; left: 150px; top: 120px; width: 460px; color: var(--white); }
  .hero-copy h1 { font-size: 30px; font-weight: 600; line-height: 1.2; }
  .hero-copy p { font-size: 13px; margin-top: 14px; line-height: 1.5; opacity: .9; width: 400px; }
  .explore-btn { display: inline-block; margin-top: 24px; border: 1.5px solid var(--white); border-radius: 18px; padding: 7px 18px; font-size: 10px; font-weight: 700; text-transform: uppercase; letter-spacing: .8px; color: var(--white); }
  .slider-nav { position: absolute; right: 70px; top: 120px; display: flex; flex-direction: column; gap: 14px; }
  .slider-nav span { width: 30px; height: 30px; border-radius: 50%; display: flex; align-items: center; justify-content: center; }
  .slider-nav .prev { border: 1.5px solid var(--white); }
  .slider-nav .next { background: var(--white); }

  /* Offer */
  .offer { position: absolute; top: 540px; left: 0; width: 100%; height: 360px; background: var(--red); }
  .offer-title { position: absolute; top: 30px; width: 100%; display: flex; justify-content: center; align-items: center; gap: 18px; color: var(--white); font-size: 24px; font-weight: 600; }
  .offer-title::before, .offer-title::after { content: ""; width: 70px; height: 1.5px; background: rgba(255,255,255,.8); }
  .offer-cards { position: absolute; top: 98px; left: 150px; width: 900px; display: flex; gap: 12px; }
  .card { flex: 1; background: var(--white); }
  .card-photo { height: 178px; }
  .card-photo.cyl { background: linear-gradient(135deg, #d9722a, #5a6f8a 60%, #2c3e5a); }
  .card-photo.pneu { background: linear-gradient(135deg, #e6e6e6, #8d9196 55%, #3f4347); }
  .card-photo.pump { background: linear-gradient(135deg, #9aa0a5, #3657b5 55%, #6c7073); }
  .card h3 { text-align: center; font-size: 15px; font-weight: 700; color: var(--ink); padding: 20px 0 6px; }
  .card .dots { display: flex; justify-content: center; gap: 3px; padding-bottom: 14px; }
  .card .dots i { width: 4px; height: 4px; border-radius: 50%; background: var(--grey); display: block; }
  .offer-arrow { position: absolute; top: 262px; width: 30px; height: 30px; border-radius: 50%; display: flex; align-items: center; justify-content: center; }
  .offer-arrow.left { left: 135px; background: var(--white); border: 1px solid #ddd; }
  .offer-arrow.right { right: 135px; background: #555a5e; }
</style>
</head>
<body>
<div class="site">
  <header class="site-header">
    <div class="brand">
      <span class="brand-mark"></span>
      <span class="brand-name">Brackenford<br>Fluidworks</span>
    </div>
    <div class="top-bar">
      <div class="call">Call Us:
        <svg width="16" height="16" viewBox="0 0 16 16"><circle cx="8" cy="8" r="8" fill="#ec1f27"/><path d="M5.2 4.2l1.4-.4 1 2-1 .8a5 5 0 0 0 2.4 2.4l.8-1 2 1-.4 1.4c-3.4.4-6.6-2.8-6.2-6.2z" fill="#fff"/></svg>
        <span>555-204-7318</span>
      </div>
      <div class="social"><i></i><i></i><i></i></div>
      <div class="quote-btn">Request a Quote</div>
    </div>
    <nav class="main-nav">
      <a class="active" href="#">Home</a>
      <a href="#">About Us</a>
      <a href="#">Services</a>
      <a href="#">Partner</a>
      <a href="#">Gallery</a>
      <a href="#">Blog</a>
      <a href="#">Contact</a>
    </nav>
  </header>

  <section class="hero">
    <div class="hero-photo" role="img" aria-label="Photograph of an industrial plant with steel pipework and valves"></div>
    <div class="hero-shade"></div>
    <div class="hero-copy">
      <h1>Our Services<br>Range From Large Industrial</h1>
      <p>We also offer removal and install of cylinders along with free pick up and delivery.</p>
      <span class="explore-btn">Explore More</span>
    </div>
    <div class="slider-nav">
      <span class="prev"><svg width="10" height="10" viewBox="0 0 10 10"><path d="M6.5 1.5L3 5l3.5 3.5" stroke="#fff" stroke-width="1.6" fill="none"/></svg></span>
      <span class="next"><svg width="10" height="10" viewBox="0 0 10 10"><path d="M3.5 1.5L7 5 3.5 8.5" stroke="#333" stroke-width="1.6" fill="none"/></svg></span>
    </div>
  </section>

  <section class="offer">
    <h2 class="offer-title">What We Offer</h2>
    <div class="offer-cards">
      <article class="card">
        <div class="card-photo cyl" role="img" aria-label="Photograph of a hydraulic cylinder being repaired"></div>
        <h3>Hydraulic Cylinders</h3>
        <div class="dots"><i></i><i></i><i></i><i></i></div>
      </article>
      <article class="card">
        <div class="card-photo pneu" role="img" aria-label="Photograph of pneumatic cylinders in a workshop"></div>
        <h3>Pneumatic Cylinders</h3>
        <div class="dots"><i></i><i></i><i></i><i></i></div>
      </article>
      <article class="card">
        <div class="card-photo pump" role="img" aria-label="Photograph of blue hydraulic pumps and valves"></div>
        <h3>Hydraulic Pumps</h3>
        <div class="dots"><i></i><i></i><i></i><i></i></div>
      </article>
    </div>
    <span class="offer-arrow left"><svg width="10" height="10" viewBox="0 0 10 10"><path d="M6.5 1.5L3 5l3.5 3.5" stroke="#333" stroke-width="1.6" fill="none"/></svg></span>
    <span class="offer-arrow right"><svg width="10" height="10" viewBox="0 0 10 10"><path d="M3.5 1.5L7 5 3.5 8.5" stroke="#fff" stroke-width="1.6" fill="none"/></svg></span>
  </section>
</div>
</body>
</html>
```